Marlowe's Classic Dressing

We are looking for a new label as we switch or glass bottle from a traditional bottle to a round bottle. We want to create a newer/ more appealing logo, while still maintaining some of our old label features to ensure that the brand awareness is not lost. We like the coloring of the blue and white, but feel free to play around with other colors in the design.
We are looking to add product features to our label such as "Gluten-Free", "Original Recipe From 1957" "Family Owned". With this being an older company we would like to keep the traditional feel of our label with some added modern touches.
We are not married to the greek logo/ building but would love some designs with and without it.
WE ARE LOOKING FOR A ROUND LABEL. The pictures provided below are of the old bottle.
There is a picture of the ringneck bottle below. The size of the label is 4.00 x 7.00.

```html
<!DOCTYPE html>
<html lang="en">
<head>
<meta charset="utf-8">
<title>Marlowe's Classic Dressing – Greek Dressing Label</title>
<link rel="stylesheet" href="https://fonts.googleapis.com/css2?family=Graduate&family=Oswald:wght@500;700&family=Yellowtail&family=Roboto:ital,wght@0,400;0,700;0,900;1,400&display=swap">
<style>
  :root {
    --label-blue: #1855ff;
    --accent-red: #ff3511;
    --ink-white: #ffffff;
  }
  * { margin: 0; padding: 0; box-sizing: border-box; }
  html, body { width: 1200px; height: 686px; overflow: hidden; background: var(--label-blue); }
  .label { position: relative; width: 1200px; height: 686px; background: var(--label-blue); color: var(--ink-white); }

  .brand-name {
    position: absolute; left: 0; width: 1176px; top: 54px; text-align: center;
    font-family: "Oswald", sans-serif; font-weight: 700; font-size: 62px; line-height: 1;
    color: var(--accent-red); letter-spacing: 1px;
  }
  .family-badge { position: absolute; left: 480px; top: 196px; width: 222px; height: 72px; }

  .product-name {
    position: absolute; left: 0; width: 1182px; text-align: center;
    font-family: "Graduate", serif; color: var(--ink-white); line-height: 1;
  }
  .product-name--main { top: 302px; font-size: 96px; letter-spacing: -2px; }
  .product-name--sub { top: 410px; font-size: 54px; letter-spacing: -1px; }

  .heritage-line {
    position: absolute; left: 0; width: 1182px; top: 500px; text-align: center;
    font-family: "Yellowtail", cursive; font-size: 34px; line-height: 1;
  }
  .divider { position: absolute; left: 438px; top: 560px; width: 307px; height: 2px; background: var(--ink-white); border-radius: 50%; }
  .claims {
    position: absolute; left: 0; width: 1182px; top: 581px; text-align: center;
    font-family: "Oswald", sans-serif; font-weight: 500; font-size: 19px; letter-spacing: 3.5px; line-height: 1;
  }
  .volume-band {
    position: absolute; left: 0; top: 625px; width: 1200px; height: 46px; background: var(--accent-red);
    display: flex; align-items: center; justify-content: center;
    font-family: "Oswald", sans-serif; font-weight: 500; font-size: 18px; letter-spacing: 3.5px;
  }

  .nutrition-panel {
    position: absolute; left: 897px; top: 38px; width: 264px; height: 420px;
    border: 2px solid var(--ink-white); padding: 4px 6px 0 8px;
    font-family: "Roboto", sans-serif; color: var(--ink-white);
  }
  .nutrition-panel__title { font-weight: 900; font-size: 28.5px; line-height: 1; letter-spacing: 1px; padding-bottom: 2px; border-bottom: 1.5px solid var(--ink-white); }
  .nutrition-panel__serving { font-size: 14px; line-height: 17px; margin-top: 3px; }
  .bar-thick { height: 6px; background: var(--ink-white); margin: 3px 0 2px; }
  .nutrition-panel__amount { font-size: 11px; font-weight: 700; line-height: 14px; }
  .calories { display: flex; justify-content: space-between; align-items: baseline; font-weight: 700; line-height: 30px; }
  .calories__label { font-size: 23px; }
  .calories__value { font-size: 32px; }
  .dv-head { font-size: 8.5px; font-weight: 700; text-align: right; padding: 4px 2px 2px 0; border-bottom: 1px solid var(--ink-white); }
  .nutrient { display: flex; justify-content: space-between; font-size: 11.5px; line-height: 16.6px; border-bottom: 1px solid var(--ink-white); padding-right: 10px; }
  .nutrient:last-of-type { border-bottom: none; }
  .nutrient b { font-weight: 700; }
  .nutrient--indent { padding-left: 15px; }
  .nutrient--indent2 { padding-left: 29px; }
  .nutrient__dv { font-weight: 700; }
  .footnote { font-size: 8.3px; line-height: 11px; margin-top: 6px; }
</style>
</head>
<body>
<main class="label">
  <div class="brand-name">Marlowe's</div>

  <svg class="family-badge" viewBox="0 0 222 72" aria-label="Family Owned">
    <defs><path id="badge-arc" d="M18 52 A110 80 0 0 1 204 52"/></defs>
    <text font-family="Oswald, sans-serif" font-weight="700" font-size="20" fill="#fff" letter-spacing="3">
      <textPath href="#badge-arc" startOffset="50%" text-anchor="middle">FAMILY OWNED</textPath>
    </text>
    <circle cx="11" cy="58" r="2.5" fill="#fff"/>
    <circle cx="212" cy="58" r="2.5" fill="#fff"/>
    <circle cx="88" cy="62" r="4.5" fill="#fff"/>
    <circle cx="112" cy="62" r="4.5" fill="#fff"/>
    <circle cx="136" cy="62" r="4.5" fill="#fff"/>
  </svg>

  <h1 class="product-name product-name--main">GREEK</h1>
  <h2 class="product-name product-name--sub">DRESSING</h2>

  <p class="heritage-line">Original Recipe From 1957</p>
  <div class="divider"></div>
  <p class="claims">•GLUTEN FREE • ALL-NATURAL•</p>

  <div class="volume-band">12 FL.OZ (354 ML)</div>

  <section class="nutrition-panel">
    <div class="nutrition-panel__title">Nutrition Facts</div>
    <div class="nutrition-panel__serving"><b>Serving size &nbsp;2 Tbsp (31g)</b><br>Servings per container: <b>8</b></div>
    <div class="bar-thick"></div>
    <div class="nutrition-panel__amount">Amount Per Serving</div>
    <div class="calories"><span class="calories__label">Calories</span><span class="calories__value">150</span></div>
    <div class="bar-thick" style="height:5px"></div>
    <div class="dv-head">% Daily Value*</div>
    <div class="nutrient"><span><b>Total Fat</b> 17g</span><span class="nutrient__dv">22%</span></div>
    <div class="nutrient nutrient--indent"><span>Saturated Fat 2.5g</span><span class="nutrient__dv">13%</span></div>
    <div class="nutrient nutrient--indent"><span><i>Trans</i> Fat 0g</span><span></span></div>
    <div class="nutrient"><span><b>Cholesterol</b> 0mg</span><span class="nutrient__dv">0%</span></div>
    <div class="nutrient"><span><b>Sodium</b> 160mg</span><span class="nutrient__dv">7%</span></div>
    <div class="nutrient"><span><b>Total Carbohydrate</b> 1g</span><span class="nutrient__dv">0%</span></div>
    <div class="nutrient nutrient--indent"><span>Dietary Fiber 0g</span><span class="nutrient__dv">0%</span></div>
    <div class="nutrient nutrient--indent"><span>Total Sugars 1g</span><span></span></div>
    <div class="nutrient nutrient--indent2"><span>Includes 0g Added Sugars</span><span class="nutrient__dv">0%</span></div>
    <div class="nutrient"><span><b>Protein</b> 0g</span><span class="nutrient__dv">0%</span></div>
    <div class="bar-thick" style="margin-top:2px"></div>
    <p class="footnote">Not a significant source of vitamin D, calcium, iron, and potassium<br>* The % Daily Value (DV) tells you how a nutrient in a serving of food contributes to a daily diet. 2,000 calories a day is used for general nutrition advice.</p>
  </section>
</main>
</body>
</html>
```